stars + comments Reviews website design (similar to quarn concept)

Please refer to attached logo and wire frames
----------------------------------------------------------------------------------------------------
we are a company based in egypt, seeking a design for a website that allows user to find doctors using search and filters.
also it allows user to review this doctor through providing comment and 1 to 5 stars
i need 4 main pages designs:
1- Doctors list/favorites list
2- Doctor view
3- Add doctor (3 steps)
4- Sign-in/sign up
5- Menu design
am into the colors teal/turquoise (though am open for different opinion)
i don't want the design theme to be doctors specific
am into the school of very clean, very neat, very simple
(plombex, ruvanteo, melvoshade designs are appealing to me)

Number of Pages Required

4 page

Font styles to use
Sans Serif

Colors
00a990
33b8a4

Requirements
Must have
• website will be bilingual/ bi-directional (English and Arabic)
• designer needs to provide another copy of the design with "right to left" orientation
• interactive button animation

```html
<!DOCTYPE html>
<html lang="en">
<head>
<meta charset="utf-8">
<title>Curavio – Add Address and Schedule</title>
<link rel="stylesheet" href="https://fonts.googleapis.com/css2?family=Open+Sans:wght@400;600;700&display=swap">
<style>
:root{
  --teal:#00a990;
  --teal-dark:#009a83;
  --teal-light:#33b8a4;
  --amber:#f6b41a;
  --page:#f5f5f5;
  --card:#ffffff;
  --line:#e2e2e2;
  --field-border:#c9c9c9;
  --text:#444444;
  --muted:#666666;
  --faint:#c4c4c4;
  --white:#ffffff;
}
*{box-sizing:border-box;margin:0;padding:0}
html,body{width:1200px;height:652px;overflow:hidden}
body{position:relative;background:var(--page);font-family:"Open Sans",Arial,sans-serif;color:var(--text)}
a{text-decoration:none}

/* header */
.site-header{position:absolute;left:0;top:0;width:1200px;height:53px;background:var(--teal)}
.brand{position:absolute;left:192px;top:0;width:151px;height:53px;background:var(--teal-dark);display:flex;align-items:center;padding-left:17px;gap:6px;color:var(--white);font-size:23px;font-weight:400;letter-spacing:.2px}
.brand-dot{width:8px;height:8px;border-radius:50%;background:var(--white)}
.nav-item{position:absolute;top:20px;display:flex;align-items:center;gap:5px;color:#cdeee8;font-size:10.5px;line-height:14px;white-space:nowrap}
.nav-item.active{color:var(--white)}
.nav-item svg{width:9px;height:9px;fill:currentColor;flex:none}
.user-name{position:absolute;left:887px;top:19px;font-size:10.5px;font-weight:600;color:var(--white)}
.avatar{position:absolute;left:957px;top:10px;width:33px;height:33px;border-radius:50%;border:2px solid var(--white);background:linear-gradient(135deg,#5b6a72,#2c3338)}
.caret{position:absolute;left:996px;top:24px;width:0;height:0;border-left:3.5px solid transparent;border-right:3.5px solid transparent;border-top:4px solid var(--white)}

/* steps */
.steps-bar{position:absolute;left:0;top:53px;width:1200px;height:55px;background:var(--white);border-bottom:1px solid var(--line)}
.step-link{position:absolute;top:80px;height:1px;background:#bdbdbd}
.step{position:absolute;top:67px;width:113px;height:27px;border:1.5px solid #b9b9b9;border-radius:14px;background:var(--white);font-size:10.5px;font-weight:600;color:var(--text);display:flex;align-items:center;justify-content:center;gap:4px}
.step.done{color:var(--teal)}
.step.current{border-color:var(--amber);color:var(--amber)}
.step svg{width:9px;height:9px}

/* card */
.page-title{position:absolute;left:209px;top:141px;font-size:13px;font-weight:400;color:var(--text)}
.form-card{position:absolute;left:210px;top:167px;width:781px;height:349px;background:var(--card);border:1px solid var(--line);border-radius:4px}
.col-divider{position:absolute;left:625px;top:183px;width:1px;height:240px;background:var(--line)}
.card-footer-rule{position:absolute;left:211px;top:443px;width:779px;height:1px;background:var(--line)}
.field-label{position:absolute;font-size:10px;font-weight:700;color:var(--muted);line-height:12px}
.select,.input{position:absolute;height:29px;border:1px solid var(--field-border);border-radius:4px;background:var(--white);font-size:8.5px;color:var(--muted);display:flex;align-items:center;padding-left:9px}
.select svg{position:absolute;right:7px;top:9px;width:11px;height:11px}
.add-phone{position:absolute;left:410px;top:395px;width:163px;height:27px;border-radius:14px;background:#eeeeee;color:var(--muted);font-size:10px;display:flex;align-items:center;justify-content:center;gap:5px}

/* schedule */
.day-row{position:absolute;left:676px;width:268px;height:29px}
.day-check{position:absolute;left:0;top:4px;width:21px;height:21px;border:1px solid var(--field-border);border-radius:6px;background:var(--white)}
.day-check.on{border-color:var(--teal-light)}
.day-check svg{position:absolute;left:4px;top:4px;width:12px;height:12px}
.day-name{position:absolute;left:29px;top:8px;font-size:8.5px;line-height:12px;color:var(--muted)}
.time{width:68px;height:29px;top:0;padding-left:7px}
.time.from{left:113px}
.time.to{left:200px}

.btn{position:absolute;top:463px;height:28px;border-radius:14px;font-size:10px;display:flex;align-items:center;justify-content:center;gap:4px}
.btn svg{width:9px;height:9px}
.btn-prev{left:598px;width:179px;background:#f5f5f5;color:var(--faint)}
.btn-next{left:796px;width:180px;background:var(--amber);color:#3a2c05}
.btn b{font-weight:700}

/* footer */
.site-footer{position:absolute;left:0;top:568px;width:1200px;height:84px;background:var(--white);border-top:1px solid var(--line)}
.copyright{position:absolute;left:209px;top:605px;font-size:10px;line-height:13px;color:var(--muted)}
.social-like{position:absolute;left:366px;top:605px;width:57px;height:14px;border-radius:2px;background:#ececec;border:1px solid #d5d5d5}
.social-follow{position:absolute;left:440px;top:605px;width:94px;height:14px;border-radius:3px;background:#ececec;border:1px solid #d5d5d5}
.footer-link{position:absolute;top:605px;font-size:9.8px;line-height:13px;color:var(--muted)}
</style>
</head>
<body>

<header class="site-header">
  <div class="brand"><span>Curavio</span><span class="brand-dot"></span></div>
  <nav class="main-nav">
    <a class="nav-item" style="left:411px"><svg viewBox="0 0 10 10"><path d="M5 0.5 0 5h1.5v4.5h2.5V6.5h2v3h2.5V5H10z"/></svg>Home</a>
    <a class="nav-item" style="left:476px"><svg viewBox="0 0 10 10"><path d="M5 9.3 1 5.3A2.4 2.4 0 0 1 5 2a2.4 2.4 0 0 1 4 3.3z"/></svg>Favorites</a>
    <a class="nav-item active" style="left:552px"><svg viewBox="0 0 10 10"><circle cx="5" cy="5" r="5"/><path d="M5 2.5v5M2.5 5h5" stroke="#00a990" stroke-width="1.5"/></svg>Add Doctor</a>
  </nav>
  <span class="user-name">Omar Hale</span>
  <div class="avatar" role="img" aria-label="User profile photo"></div>
  <span class="caret"></span>
</header>

<div class="steps-bar"></div>
<div class="step-link" style="left:456px;width:88px"></div>
<div class="step-link" style="left:656px;width:88px"></div>
<div class="step done" style="left:344px"><svg viewBox="0 0 12 12"><path d="M1.5 6.5 4.5 9.5 10.5 2.5" fill="none" stroke="#00a990" stroke-width="2.2"/></svg>Basic Info</div>
<div class="step current" style="left:544px">Address</div>
<div class="step" style="left:744px">Review</div>

<h1 class="page-title">Add Address and Schedule</h1>

<section class="form-card"></section>
<div class="col-divider"></div>
<div class="card-footer-rule"></div>

<span class="field-label" style="left:230px;top:186px">Country</span>
<div class="select" style="left:230px;top:205px;width:161px">Select Country<svg viewBox="0 0 12 12"><path d="M2 4l4 4 4-4" fill="none" stroke="#444" stroke-width="2"/></svg></div>
<span class="field-label" style="left:410px;top:186px">Province / State</span>
<div class="select" style="left:410px;top:205px;width:162px">Select Province<svg viewBox="0 0 12 12"><path d="M2 4l4 4 4-4" fill="none" stroke="#444" stroke-width="2"/></svg></div>

<span class="field-label" style="left:230px;top:249px">City</span>
<div class="select" style="left:230px;top:269px;width:161px">Select City<svg viewBox="0 0 12 12"><path d="M2 4l4 4 4-4" fill="none" stroke="#444" stroke-width="2"/></svg></div>
<span class="field-label" style="left:408px;top:249px">Neighborhood</span>
<div class="select" style="left:410px;top:269px;width:162px">Select Neighborhood<svg viewBox="0 0 12 12"><path d="M2 4l4 4 4-4" fill="none" stroke="#444" stroke-width="2"/></svg></div>

<span class="field-label" style="left:230px;top:313px">Address</span>
<div class="input" style="left:229px;top:330px;width:343px"></div>

<span class="field-label" style="left:230px;top:375px">Phone Number</span>
<div class="input" style="left:230px;top:394px;width:161px"></div>
<div class="add-phone"><svg viewBox="0 0 10 10" width="9" height="9"><path d="M5 1v8M1 5h8" stroke="#555" stroke-width="2"/></svg>Add Another Phone</div>

<span class="field-label" style="left:676px;top:186px">Schedule</span>

<div class="day-row" style="top:205px"><span class="day-check on"><svg viewBox="0 0 12 12"><path d="M1.5 6.5 4.5 9.5 10.5 2.5" fill="none" stroke="#00a990" stroke-width="2.2"/></svg></span><span class="day-name">Sunday</span><div class="select time from">00:00<svg viewBox="0 0 12 12"><path d="M2 4l4 4 4-4" fill="none" stroke="#444" stroke-width="2"/></svg></div><div class="select time to">00:00<svg viewBox="0 0 12 12"><path d="M2 4l4 4 4-4" fill="none" stroke="#444" stroke-width="2"/></svg></div></div>
<div class="day-row" style="top:237px"><span class="day-check"></span><span class="day-name">Monday</span><div class="select time from">00:00<svg viewBox="0 0 12 12"><path d="M2 4l4 4 4-4" fill="none" stroke="#444" stroke-width="2"/></svg></div><div class="select time to">00:00<svg viewBox="0 0 12 12"><path d="M2 4l4 4 4-4" fill="none" stroke="#444" stroke-width="2"/></svg></div></div>
<div class="day-row" style="top:270px"><span class="day-check on"><svg viewBox="0 0 12 12"><path d="M1.5 6.5 4.5 9.5 10.5 2.5" fill="none" stroke="#00a990" stroke-width="2.2"/></svg></span><span class="day-name">Tuesday</span><div class="select time from">00:00<svg viewBox="0 0 12 12"><path d="M2 4l4 4 4-4" fill="none" stroke="#444" stroke-width="2"/></svg></div><div class="select time to">00:00<svg viewBox="0 0 12 12"><path d="M2 4l4 4 4-4" fill="none" stroke="#444" stroke-width="2"/></svg></div></div>
<div class="day-row" style="top:302px"><span class="day-check on"><svg viewBox="0 0 12 12"><path d="M1.5 6.5 4.5 9.5 10.5 2.5" fill="none" stroke="#00a990" stroke-width="2.2"/></svg></span><span class="day-name">Wednesday</span><div class="select time from">00:00<svg viewBox="0 0 12 12"><path d="M2 4l4 4 4-4" fill="none" stroke="#444" stroke-width="2"/></svg></div><div class="select time to">00:00<svg viewBox="0 0 12 12"><path d="M2 4l4 4 4-4" fill="none" stroke="#444" stroke-width="2"/></svg></div></div>
<div class="day-row" style="top:334px"><span class="day-check"></span><span class="day-name">Thursday</span><div class="select time from">00:00<svg viewBox="0 0 12 12"><path d="M2 4l4 4 4-4" fill="none" stroke="#444" stroke-width="2"/></svg></div><div class="select time to">00:00<svg viewBox="0 0 12 12"><path d="M2 4l4 4 4-4" fill="none" stroke="#444" stroke-width="2"/></svg></div></div>
<div class="day-row" style="top:367px"><span class="day-check on"><svg viewBox="0 0 12 12"><path d="M1.5 6.5 4.5 9.5 10.5 2.5" fill="none" stroke="#00a990" stroke-width="2.2"/></svg></span><span class="day-name">Friday</span><div class="select time from">00:00<svg viewBox="0 0 12 12"><path d="M2 4l4 4 4-4" fill="none" stroke="#444" stroke-width="2"/></svg></div><div class="select time to">00:00<svg viewBox="0 0 12 12"><path d="M2 4l4 4 4-4" fill="none" stroke="#444" stroke-width="2"/></svg></div></div>
<div class="day-row" style="top:399px"><span class="day-check on"><svg viewBox="0 0 12 12"><path d="M1.5 6.5 4.5 9.5 10.5 2.5" fill="none" stroke="#00a990" stroke-width="2.2"/></svg></span><span class="day-name">Saturday</span><div class="select time from">00:00<svg viewBox="0 0 12 12"><path d="M2 4l4 4 4-4" fill="none" stroke="#444" stroke-width="2"/></svg></div><div class="select time to">00:00<svg viewBox="0 0 12 12"><path d="M2 4l4 4 4-4" fill="none" stroke="#444" stroke-width="2"/></svg></div></div>

<a class="btn btn-prev"><svg viewBox="0 0 10 10"><path d="M9 5H2M5 1.5 1.5 5 5 8.5" fill="none" stroke="#c4c4c4" stroke-width="2"/></svg>Previous Step : <b>Edit Info</b></a>
<a class="btn btn-next"><svg viewBox="0 0 10 10"><path d="M1 5h7M5 1.5 8.5 5 5 8.5" fill="none" stroke="#3a2c05" stroke-width="2"/></svg>Next Step : <b>Add Review</b></a>

<footer class="site-footer"></footer>
<span class="copyright">Copyrights 2015. Curavio.com</span>
<span class="social-like" role="img" aria-label="Social like button"></span>
<span class="social-follow" role="img" aria-label="Social follow button"></span>
<a class="footer-link" style="left:655px">Home</a>
<a class="footer-link" style="left:703px">Favorite</a>
<a class="footer-link" style="left:751px">Add Doctor</a>
<a class="footer-link" style="left:823px">Terms of Use</a>
<a class="footer-link" style="left:898px">FAQ</a>
<a class="footer-link" style="left:943px">Contact Us</a>

</body>
</html>
```